Aquatic View

We need a web design for a new window cleaning company name Bright Pane Services. We are located in Grand Cayman, Cayman Islands. We are a small company, a team of husband and wife. Our services include residencial interior and exterior window cleaning and commercial. Extra services such as ceiling fans cleaning, mirrors, high dusting. Home cleaning services. Power washing. Explaining the service. We want a modern, beachy style with aquatic colors. We want to use our domain name "brightpaneservices.ky". We want to portray a clean, modern and professional design.

Target Market(s)

Big Home owners

Industry/Entity Type

Cleaning Service

Contact Information for Business Card

Company Name: Bright Pane Services
Name: Gerald Thornbury owner/manager
Phone: 345-9418372
Email: gerald@brightpaneservices.ky
Website: brightpaneservices.ky
Address: P.O.Box 2846 GT, George Town, Grand Cayman KY1-1304 Cayman Islands

Number of Pages Required

2 page

Font styles to use
Sans Serif

Colors
0592cd
0455a3
33a6d7
85cae6
cadf82
abd036
fbf289

Requirements
Nice to have
• Pictures of an ocean view and palm trees from clear windows.
• https://quotrelvane.com/estimately/
• Use the above for "free estimate".

```html
<!DOCTYPE html>
<html lang="en">
<head>
<meta charset="utf-8">
<title>Bright Pane Services</title>
<link href="https://fonts.googleapis.com/css2?family=PT+Sans:wght@400;700&family=Tinos&display=swap" rel="stylesheet">
<style>
:root{
  --ink:#3d3d3d;
  --body:#4a4a4a;
  --sky:#33a6d7;
  --blue:#3a87c8;
  --icon:#9fd0ea;
  --green:#80bd2a;
  --title-green:#77b22e;
  --band:#efefef;
  --footer:#4b5967;
  --footer-line:#c9ced3;
  --base:#0f2c48;
  --white:#ffffff;
  --dot:#6b6b6b;
}
*{margin:0;padding:0;box-sizing:border-box}
html,body{width:963px;height:1200px;overflow:hidden;background:var(--white)}
body{font-family:"PT Sans",sans-serif;color:var(--body);position:relative}
.abs{position:absolute}
.btn{position:absolute;display:flex;align-items:center;justify-content:center;color:var(--white);font-family:"Tinos",serif;font-size:16px;letter-spacing:.3px}
.btn-green{background:var(--green)}
.btn-blue{background:var(--blue)}

/* header */
.site-header{position:absolute;left:0;top:0;width:963px;height:93px;background:var(--white)}
.brand{position:absolute;left:92px;top:34px;display:flex;align-items:center;gap:7px;font-size:15px;font-weight:700;color:var(--ink)}
.brand-mark{width:18px;height:18px;border-radius:50%;background:var(--sky)}
.main-nav{position:absolute;top:53px;left:0;font-size:15px;color:var(--ink);text-transform:uppercase}
.main-nav span{position:absolute;white-space:nowrap}
.header-phone{position:absolute;left:680px;top:48px;display:flex;align-items:center;gap:18px;color:var(--sky);font-size:21px}

/* hero */
.hero{position:absolute;left:0;top:93px;width:963px;height:268px;background:linear-gradient(180deg,#6fc4ec 0%,#3a9fd6 45%,#2f86bf 62%,#d9d4c8 78%,#c7c0b2 100%)}
.hero-text{position:absolute;left:103px;top:45px;width:330px;font-size:25px;line-height:31.5px;color:var(--white);text-shadow:0 2px 3px rgba(0,0,0,.45)}

/* slider band */
.intro{position:absolute;left:0;top:361px;width:963px;height:243px;background:var(--band)}
.intro-photo{position:absolute;left:104px;top:29px;width:254px;height:169px;border:1px solid #333;background:linear-gradient(135deg,#e8e6de 0%,#9bbf7a 40%,#6e8a4c 60%,#b88a52 100%)}
.intro h2{position:absolute;left:457px;top:23px;width:260px;font-size:20px;font-weight:400;line-height:24px;color:var(--ink)}
.intro p{position:absolute;left:457px;top:88px;width:360px;font-size:13.5px;line-height:16.5px;color:var(--ink)}
.dot{position:absolute;top:216px;width:13px;height:13px;border-radius:50%;background:var(--dot)}
.dot.active{background:var(--blue)}

/* services */
.services-title{position:absolute;left:0;top:630px;width:963px;text-align:center;font-size:30px;color:var(--title-green)}
.service h3{position:absolute;font-size:12px;font-weight:700;line-height:15px;color:var(--blue);text-transform:uppercase;width:200px}
.service p{position:absolute;font-size:12.5px;line-height:15px;color:var(--body)}

/* footer */
.site-footer{position:absolute;left:0;top:960px;width:963px;height:208px;background:var(--footer)}
.footer-nav a{position:absolute;top:22px;font-size:14.5px;color:var(--white);text-decoration:none;text-align:center;width:62px;padding-bottom:6px;border-bottom:2px solid var(--footer-line)}
.social{position:absolute;border-radius:50%;background:#c8c8c8}
.footer-contact{position:absolute;left:384px;color:var(--white);font-size:14px;display:flex;align-items:center;gap:30px}
.field{position:absolute;left:654px;width:235px;background:var(--white);font-size:12px;color:#666;padding:7px 9px}
.legal{position:absolute;left:0;top:1168px;width:963px;height:32px;background:var(--base);color:var(--white);font-size:11px;padding:10px 0 0 104px}
</style>
</head>
<body>

<header class="site-header">
  <div class="brand"><span class="brand-mark"></span>Bright Pane Services</div>
  <nav class="main-nav">
    <span style="left:287px">Home</span>
    <span style="left:364px">About</span>
    <span style="left:437px">Services</span>
    <span style="left:521px">Contact</span>
  </nav>
  <div class="header-phone">
    <svg width="26" height="20" viewBox="0 0 26 20"><path d="M2 7c0-4 22-4 22 0v2h-5V6H7v3H2z" fill="#3a87c8"/><path d="M6 9h14l3 9H3z" fill="#3a87c8"/><circle cx="13" cy="13" r="3" fill="#fff"/></svg>
    <span>9847 610382</span>
  </div>
</header>

<section class="hero" role="img" aria-label="Bright living room with a white sofa and cushions beside tall clear windows overlooking the ocean">
  <p class="hero-text">Extra services such as ceiling fans cleaning, mirrors, high dusting. Home cleaning services. Power washing.</p>
  <a class="btn btn-green" style="left:103px;top:191px;width:143px;height:42px">ABOUT US</a>
</section>

<section class="intro">
  <svg class="abs" style="left:0;top:55px" width="49" height="93" viewBox="0 0 49 93"><path d="M0 0L49 46.5L0 93z" fill="#3a87c8"/><path d="M15 38l-4 8.5 4 8.5" stroke="#fff" stroke-width="2.5" fill="none"/></svg>
  <svg class="abs" style="left:914px;top:55px" width="49" height="93" viewBox="0 0 49 93"><path d="M49 0L0 46.5L49 93z" fill="#3a87c8"/><path d="M34 38l4 8.5-4 8.5" stroke="#fff" stroke-width="2.5" fill="none"/></svg>
  <div class="intro-photo" role="img" aria-label="Couple and their dog looking out of a bay window onto a green garden"></div>
  <h2>We are located in Grand Cayman, Cayman Islands.</h2>
  <p>We are a small company, a team of husband and wife.<br>Our services include residencial interior<br>and exterior window cleaning and commercial.</p>
  <a class="btn btn-blue" style="left:456px;top:156px;width:144px;height:41px">LEARN MORE</a>
  <span class="dot" style="left:387px"></span>
  <span class="dot active" style="left:421px"></span>
  <span class="dot" style="left:454px"></span>
  <span class="dot" style="left:488px"></span>
  <span class="dot" style="left:521px"></span>
</section>

<h2 class="services-title">Our services</h2>

<div class="service">
  <svg class="abs" style="left:139px;top:684px" width="56" height="54" viewBox="0 0 56 54" fill="#9fd0ea"><path d="M28 2L2 24h6v30h40V24h6z"/><g fill="#fff"><rect x="14" y="26" width="6" height="6"/><rect x="25" y="26" width="6" height="6"/><rect x="36" y="26" width="6" height="6"/><rect x="14" y="38" width="6" height="6"/><rect x="36" y="38" width="6" height="6"/><rect x="25" y="38" width="6" height="16"/></g></svg>
  <h3 style="left:104px;top:768px">We are located in Grand Cayman, Cayman Islands.</h3>
  <p style="left:104px;top:812px;width:220px">We are a small company, a team of husband and wife. Our services include residencial interior<br>and exterior window cleaning<br>and commercial.</p>
</div>
<div class="service">
  <svg class="abs" style="left:417px;top:684px" width="54" height="54" viewBox="0 0 54 54" fill="#9fd0ea"><rect x="15" y="0" width="24" height="54"/><rect x="0" y="20" width="15" height="34"/><rect x="39" y="20" width="15" height="34"/><g fill="#fff"><rect x="20" y="6" width="5" height="6"/><rect x="29" y="6" width="5" height="6"/><rect x="20" y="17" width="5" height="6"/><rect x="29" y="17" width="5" height="6"/><rect x="20" y="28" width="5" height="6"/><rect x="29" y="28" width="5" height="6"/><rect x="4" y="27" width="6" height="6"/><rect x="44" y="27" width="6" height="6"/><rect x="4" y="38" width="6" height="6"/><rect x="44" y="38" width="6" height="6"/><rect x="23" y="42" width="8" height="12"/></g></svg>
  <h3 style="left:384px;top:768px">We are located in Grand Cayman, Cayman Islands.</h3>
  <p style="left:384px;top:812px;width:220px">We are a small company, a team of husband and wife. Our services include residencial interior</p>
</div>
<div class="service">
  <svg class="abs" style="left:696px;top:684px" width="48" height="54" viewBox="0 0 48 54"><rect x="19" y="0" width="10" height="5" fill="#9fd0ea"/><circle cx="24" cy="30" r="20" fill="none" stroke="#9fd0ea" stroke-width="6"/><path d="M24 30L32 20" stroke="#9fd0ea" stroke-width="4"/></svg>
  <h3 style="left:652px;top:761px">We are located in Grand Cayman, Cayman Islands.</h3>
  <p style="left:652px;top:805px;width:240px">We are a small company, a team of husband and wife. Our services include residencial interior and exterior window cleaning<br>and commercial.</p>
</div>
<a class="btn btn-green" style="left:387px;top:899px;width:144px;height:41px">LEARN MORE</a>

<footer class="site-footer">
  <nav class="footer-nav">
    <a style="left:103px">ABOUT</a>
    <a style="left:186px">SERVICES</a>
    <a style="left:269px">CONTACT</a>
  </nav>
  <span class="social" style="left:406px;top:40px;width:52px;height:52px"></span>
  <span class="social" style="left:480px;top:41px;width:53px;height:53px"></span>
  <div class="footer-contact" style="top:128px">
    <svg width="27" height="20" viewBox="0 0 26 20" fill="#c8c8c8"><path d="M2 7c0-4 22-4 22 0v2h-5V6H7v3H2z"/><path d="M6 9h14l3 9H3z"/><circle cx="13" cy="13" r="3" fill="#4b5967"/></svg>
    <span>9847 610382</span>
  </div>
  <div class="footer-contact" style="top:158px">
    <svg width="27" height="17" viewBox="0 0 27 17"><rect x="1" y="1" width="25" height="15" fill="#c8c8c8"/><path d="M1 1l12.5 9L26 1M1 16l9-7M26 16l-9-7" stroke="#4b5967" stroke-width="1.2" fill="none"/></svg>
    <span>info@brightpaneservices.ky</span>
  </div>
  <div class="field" style="top:14px;height:26px">Name</div>
  <div class="field" style="top:50px;height:26px">Email</div>
  <div class="field" style="top:87px;height:55px">Your Message</div>
  <a class="btn btn-green" style="left:745px;top:153px;width:144px;height:41px">FREE ESTIMATE</a>
</footer>

<div class="legal">© 2015 Bright Pane Services. All Rights Reserved. / Privacy Policy /</div>

</body>
</html>
```